Kavenzira Wines

A Red Wine Label for future Wine Concept called Kavenzira Wine. The back label will have the following words which capture the essence of the wine "I am sworn to the secrecy about the origins of this wine but I can assure you it’s from the best cellars of Africa. Kavenzira is an African (Shona) name which loosely means honour, praise or to be held in high exteem. Hold on to your hats because this wine is a whirlwind of flavours. It's dark, spicy and fruity flavours will attack the palate with warm aggression and intent whilst being served with Sadza/ Nsima and roasted beef accompanied with mufushwa (dried vegetables) cooked in grounded nut paste. The inspiring flame, style and mood of an African braai, together with its outlandish flavours popping in and out of the glass, Kavenzira will make every serving a gesture of respect and distinction!!!"
Updates

I will be buying wine packed in unbranded bottles then Brand it as Kavenzira on my own Kavenzira label for some African event theme. The wines will be South African a Shiraz. So I need a back label with message placed in brief and front label for a red wine bottle. I have attached some old labels for the wine so I need a redesign of the l label for have a morden and African feel to it                                   

Please

Target Market(s)

Appeal to general populace and those with an afrocentric feel

Requirements
Must have
• Back and front labels, simplicity
Should not have
• Too many colours

```html
<!DOCTYPE html>
<html lang="en">
<head>
<meta charset="utf-8">
<title>Kavenzira Wines – Shiraz Labels</title>
<link rel="stylesheet" href="https://fonts.googleapis.com/css2?family=Delius&display=swap">
<style>
  :root {
    --page: #ffffff;
    --label-face: #3c0306;
    --label-bevel: #6a0a0d;
    --label-bevel-top: #a66a6c;
    --label-bevel-dark: #4a0508;
    --label-edge: #2a0204;
    --ink: #f4efe6;
    --ink-shadow: rgba(0, 0, 0, 0.85);
    --goblet-light: #f0c9cf;
    --goblet-mid: #b8653a;
    --goblet-dark: #5a2410;
  }

  * { box-sizing: border-box; margin: 0; padding: 0; }

  html, body {
    width: 1200px;
    height: 582px;
    overflow: hidden;
    background: var(--page);
  }

  body {
    position: relative;
    font-family: "Delius", "Tempus Sans ITC", cursive;
    color: var(--ink);
  }

  .label {
    position: absolute;
    top: 23px;
    width: 512px;
    height: 512px;
    background: var(--label-face);
    border-style: solid;
    border-width: 11px;
    border-color: var(--label-bevel-top) var(--label-bevel) var(--label-bevel-dark) var(--label-bevel);
    outline: 1px solid var(--label-edge);
  }

  .label--front { left: 42px; }
  .label--back  { left: 646px; }

  .goblet-art {
    position: absolute;
    z-index: 0;
    background: radial-gradient(ellipse at 50% 28%, var(--goblet-light) 0%, var(--goblet-mid) 38%, var(--goblet-dark) 80%, transparent 100%);
    border-radius: 46% 46% 30% 30% / 40% 40% 20% 20%;
  }

  .label--front .goblet-art {
    left: 118px;
    top: 40px;
    width: 208px;
    height: 254px;
  }

  .label--back .goblet-art {
    left: 346px;
    top: 274px;
    width: 134px;
    height: 206px;
  }

  .wine-name,
  .wine-details,
  .back-story {
    z-index: 1;
  }

  .wine-name {
    position: absolute;
    left: 0;
    width: 100%;
    top: 300px;
    text-align: center;
    font-size: 44px;
    line-height: 1;
    font-weight: 400;
    text-shadow: 2px 2px 4px var(--ink-shadow);
  }

  .wine-details {
    position: absolute;
    left: 0;
    width: 100%;
    top: 368px;
    text-align: center;
    font-size: 27px;
    line-height: 33px;
    text-shadow: 2px 2px 3px var(--ink-shadow);
  }

  .label--back .wine-name,
  .label--back .wine-details {
    left: -10px;
  }

  .back-story {
    position: absolute;
    left: -11px;
    width: 512px;
    top: 17px;
    text-align: center;
    font-size: 16px;
    line-height: 20px;
    text-shadow: 1px 1px 2px var(--ink-shadow);
  }

  .back-story span {
    display: block;
    white-space: nowrap;
  }
</style>
</head>
<body>

  <section class="label label--front">
    <div class="goblet-art" role="img" aria-label="Illustration of two bronze wine goblets"></div>
    <h1 class="wine-name">Kavenzira</h1>
    <p class="wine-details">Shiraz<br>South Africa<br>2013</p>
  </section>

  <section class="label label--back">
    <div class="goblet-art" role="img" aria-label="Illustration of a bronze wine goblet"></div>
    <p class="back-story">
      <span>I am sworn to the secrecy about the origins of this wine but I can</span>
      <span>assure you it’s from the best cellars of Africa. Kavenzira is an</span>
      <span>African (Shona) name which loosely means honour, praise or to</span>
      <span>be held in high exteem. Hold on to your hats because this wine is a</span>
      <span>whirlwind of flavours. It’s dark, spicy and fruity flavours will attack</span>
      <span>the palate with warm aggression and intent whilst being served</span>
      <span>with Sadza/ Nsima and roasted beef accompanied with mufushwa</span>
      <span>(dried vegetables) cooked in grounded nut paste.</span>
      <span>The inspiring flame, style and mood of an African braai,</span>
      <span>together with its outlandish flavours popping in and out of</span>
      <span>the glass, Kavenzira will make every serving a gesture</span>
      <span>of respect and</span>
      <span>distinction!</span>
    </p>
    <h2 class="wine-name">Kavenzira</h2>
    <p class="wine-details">Shiraz<br>South Africa<br>2013</p>
  </section>

</body>
</html>
```